PowerPoint Template Needed for Investment Firm

Norvelle Capital Management is an emerging wealth management firm based in New Jersey. It offers superior investment returns to high net worth individuals and institutions by finding undervalued assets.

We recently selected a company logo which was inspired by the Tucana constellation. Beta Tucanae is a group of six stars, containing star cluster 47 Tucanae, rated the second brightest object in the sky.

Now we need a PowerPoint template with the designs for the following:

1. Title/cover page slide
2. Content slide with title
3. Section slide - to introduce a new section
4. Final slide - with contact information

The slides will be used at investor presentations, that is, to provide information about the company to potential investors. Since we are an investment firm, the design should project a sense of stability, growth and professionalism. The owner is interested in something simple yet striking, which of course is consistent with the logo. I'm thinking more conservative colors and Sans Serif fonts.

I plan on changing the status to non-refundable once I see some designs that I really like.

Target Market(s)

Wealthy individuals, probably middle aged or older, in the US

Industry/Entity Type

Conservative

Requirements
Must have
• Sans serif fonts
Clean, very professional look
Conservative colors that complement existing logo
Should not have
• Anything too busy or complicated

```html
<!DOCTYPE html>
<html lang="en">
<head>
<meta charset="UTF-8">
<title>Norvelle Capital Management – Title Slide</title>
<link rel="stylesheet" href="https://fonts.googleapis.com/css2?family=Orbitron:wght@400&family=Open+Sans:wght@600&display=swap">
<style>
  :root {
    --blue-core: #0a5cc4;
    --blue-mid: #064bb0;
    --blue-edge: #032f86;
    --white: #ffffff;
    --ink: #3a4048;
    --mark-blue: #13237a;
  }
  * { margin: 0; padding: 0; box-sizing: border-box; }
  html, body {
    width: 1200px;
    height: 900px;
    overflow: hidden;
  }
  .slide {
    position: relative;
    width: 1200px;
    height: 900px;
    background: radial-gradient(ellipse 75% 70% at 50% 55%, var(--blue-core) 0%, var(--blue-mid) 55%, var(--blue-edge) 100%);
    overflow: hidden;
  }
  .brand-square {
    position: absolute;
    left: 152px;
    top: 296px;
    width: 102px;
    height: 100px;
    background: var(--mark-blue);
    border: 3px solid var(--white);
    border-radius: 12px;
  }
  .brand-plate {
    position: absolute;
    left: 75px;
    top: 375px;
    width: 255px;
    height: 95px;
    background: var(--white);
    display: flex;
    flex-direction: column;
    align-items: center;
    justify-content: center;
    font-family: "Open Sans", Arial, sans-serif;
    font-weight: 600;
    color: var(--ink);
    line-height: 1.1;
  }
  .brand-name {
    font-size: 34px;
    letter-spacing: 2px;
    text-transform: uppercase;
  }
  .brand-tagline {
    font-size: 17px;
    margin-top: 4px;
  }
  .plate-pointer {
    position: absolute;
    left: 330px;
    top: 413px;
  }
  .slide-title {
    position: absolute;
    left: 374px;
    top: 398px;
    font-family: "Orbitron", "Arial", sans-serif;
    font-weight: 400;
    font-size: 40px;
    letter-spacing: 2px;
    color: var(--white);
    white-space: nowrap;
  }
</style>
</head>
<body>
  <main class="slide">
    <div class="brand-square" aria-hidden="true"></div>
    <div class="brand-plate">
      <span class="brand-name">Norvelle</span>
      <span class="brand-tagline">Capital Management</span>
    </div>
    <svg class="plate-pointer" width="14" height="20" viewBox="0 0 14 20" aria-hidden="true">
      <polygon points="0,0 12,10 0,20" fill="#ffffff"/>
    </svg>
    <h1 class="slide-title">PERSENTATION TITLE HERE</h1>
  </main>
</body>
</html>
```